Gourmet food made with love and care in my country kitchen

I'd like a business card designed for my small home-based food business. I have made labelling in federation blue for my food products (Labneh cheese, spicy pumpkin chutney, dukkah, caramelised onion jam, yo-Yo biscuits, chocolate mud cake etc) and have navy and white checked surrounds/borders on my brochures so would like to stick to these country colours.
Target Market(s)
Foodies who love gourmet delicacies. Everyone who enjoys a picnic that they don't have to prepare themselves.
Industry/Entity Type
Business
Contact Information for Business Card
Larkhollow Pantry
42 Tindale's Lane
Brimsworth Qld 4829
Phone Viv 07 48216597 or 0412386951
- Harrington

```html
<!DOCTYPE html>
<html lang="en">
<head>
<meta charset="utf-8">
<title>Larkhollow Pantry – Business Card</title>
<link href="https://fonts.googleapis.com/css2?family=Almendra&family=Open+Sans:wght@300;400&display=swap" rel="stylesheet">
<style>
  :root {
    --backdrop: #c9d7eb;
    --federation-blue: #1c58a6;
    --ink-blue: #1f4f9d;
    --ribbon-blue: #8fb1da;
    --ribbon-edge: #b7cce8;
    --card-white: #ffffff;
    --photo-placeholder: #dfe6ec;
  }
  * { margin: 0; padding: 0; box-sizing: border-box; }
  html, body { width: 1200px; height: 741px; overflow: hidden; }
  body { background: var(--backdrop); position: relative; font-family: "Open Sans", sans-serif; }

  .card {
    position: absolute; left: 97px; top: 99px; width: 1003px; height: 539px;
    border: 5px solid var(--federation-blue);
    background: var(--card-white);
  }
  .card-inner {
    position: absolute; left: 5px; top: 5px; right: 5px; bottom: 5px;
    border: 2px solid var(--federation-blue);
    overflow: hidden;
  }

  .hero-photo {
    position: absolute; right: 0; top: 0; width: 418px; height: 100%;
    background: linear-gradient(90deg, var(--card-white) 0%, var(--photo-placeholder) 14%, var(--photo-placeholder) 100%);
  }

  .tagline-ribbon {
    position: absolute; left: 8px; top: 13px; width: 645px; height: 112px;
    background: var(--ribbon-blue);
    clip-path: polygon(0 0, 100% 0, 96% 50%, 100% 100%, 0 100%);
    border-top: 6px solid var(--ribbon-edge);
    border-bottom: 6px solid var(--ribbon-edge);
  }
  .tagline {
    position: absolute; left: 23px; top: 49px; line-height: 40px;
    font-family: "Almendra", serif; font-size: 38px; color: var(--ink-blue);
    white-space: nowrap;
  }

  .divider {
    position: absolute; left: 550px; top: 125px; width: 5px; height: 277px;
    border-left: 2px solid var(--federation-blue);
    border-right: 2px solid var(--federation-blue);
  }

  .business-name {
    position: absolute; left: 23px; top: 180px; line-height: 66px;
    font-family: "Almendra", serif; font-size: 58px; font-weight: 400;
    color: var(--federation-blue); white-space: nowrap;
  }

  .contact-list {
    position: absolute; left: 61px; top: 288px; list-style: none;
    font-size: 23px; font-weight: 300; color: var(--ink-blue);
  }
  .contact-list li { position: relative; padding-left: 20px; height: 40px; line-height: 40px; white-space: nowrap; }
  .contact-list li::before {
    content: ""; position: absolute; left: 0; top: 16px; width: 8px; height: 8px;
    background: var(--federation-blue);
  }
  .contact-list .phone-numbers { font-weight: 400; color: var(--federation-blue); }

  .social-page {
    position: absolute; left: 29px; top: 430px; display: flex; align-items: center; gap: 12px;
    font-size: 23px; font-weight: 300; color: var(--ink-blue); white-space: nowrap;
  }
  .social-square { width: 38px; height: 38px; background: var(--federation-blue); }
</style>
</head>
<body>
  <div class="card">
    <div class="card-inner">
      <div class="hero-photo" role="img" aria-label="Photo of a rustic tomato tart on an outdoor table with a bottle of olive oil and country trees behind"></div>

      <div class="tagline-ribbon"></div>
      <p class="tagline">Gourment Food Made With Love</p>

      <div class="divider"></div>

      <h1 class="business-name">Larkhollow Pantry</h1>

      <ul class="contact-list">
        <li>42 Tindale's Lane, Mt Harlow Via Brimsworth</li>
        <li>Email: larkhollowpantry@postmail.com</li>
        <li>Phone Viv: <span class="phone-numbers">07 48216597 /0412386951</span></li>
      </ul>

      <div class="social-page">
        <span class="social-square"></span>
        <span>Larkhollow Pantry</span>
      </div>
    </div>
  </div>
</body>
</html>
```